Business Card Design for new social media business

I am looking for a new professional business card design for an exciting new company which is based on providing members with experiences of others to benefit their choice of places to visit for restaurants, bars, clubs, national monument, tourist sights, hotels and so forth.
Updates

Please submit designs as I will choose to commit the funds depending on designs.

Target Market(s)

Business Managers as well as directors alongside owners

Industry/Entity Type

Business

Requirements
Must have
• Logo design and symbols
Nice to have
• Logo / Symbol on the back of the business card and possibly the logo as if embedded/embossed on the business card.

```html
<!DOCTYPE html>
<html lang="en">
<head>
<meta charset="utf-8">
<title>Norvale Business Card</title>
<link rel="stylesheet" href="https://fonts.googleapis.com/css2?family=Open+Sans:wght@400;600&display=swap">
<style>
  :root {
    --backdrop: #2b2b2b;
    --card: #ffffff;
    --card-shade: #ececec;
    --brand-ink: #1e1e1e;
    --brand-dot: #1b63b5;
    --band-start: #f2b705;
    --band-end: #c9560e;
    --ink: #1e1e1e;
    --icon-blue: #1d7fc4;
  }
  * { box-sizing: border-box; margin: 0; padding: 0; }
  html, body { width: 1200px; height: 900px; overflow: hidden; }
  body {
    background: var(--backdrop);
    font-family: "Open Sans", Arial, sans-serif;
    color: var(--ink);
    display: flex;
    flex-direction: column;
    align-items: center;
    justify-content: center;
    gap: 40px;
  }
  .card {
    position: relative;
    width: 700px;
    height: 400px;
    background: radial-gradient(ellipse at 60% 40%, var(--card) 45%, var(--card-shade) 100%);
    overflow: hidden;
  }
  /* Back */
  .card-back { display: flex; align-items: center; justify-content: center; }
  .brand {
    display: flex;
    align-items: center;
    gap: 18px;
    font-weight: 600;
    color: var(--brand-ink);
    letter-spacing: 1px;
  }
  .brand-dot { border-radius: 50%; background: var(--brand-dot); flex: none; }
  .card-back .brand { font-size: 60px; }
  .card-back .brand-dot { width: 40px; height: 40px; }
  /* Front */
  .card-front .brand {
    position: absolute;
    left: 44px;
    top: 56px;
    font-size: 46px;
    gap: 14px;
  }
  .card-front .brand-dot { width: 32px; height: 32px; }
  .holder { position: absolute; left: 48px; top: 182px; }
  .holder-name { font-size: 26px; font-weight: 400; letter-spacing: 1px; }
  .holder-role { font-size: 19px; margin-top: 2px; }
  .contact-list { list-style: none; position: absolute; font-size: 20px; }
  .contact-list li { display: flex; align-items: center; gap: 10px; line-height: 32px; }
  .contact-list svg { width: 16px; height: 16px; flex: none; }
  .contact-personal { left: 48px; top: 276px; }
  .contact-online { left: 430px; top: 200px; font-size: 19px; }
  .band {
    position: absolute;
    left: 0; right: 0; bottom: 0;
    height: 28px;
    background: linear-gradient(90deg, var(--band-start), var(--band-end));
  }
</style>
</head>
<body>
  <section class="card card-back" aria-label="Card back">
    <div class="brand"><span class="brand-dot"></span>Norvale</div>
  </section>

  <section class="card card-front" aria-label="Card front">
    <div class="brand"><span class="brand-dot"></span>Norvale</div>

    <div class="holder">
      <p class="holder-name">MARA RENWICK</p>
      <p class="holder-role">managing director</p>
    </div>

    <ul class="contact-list contact-personal">
      <li>
        <svg viewBox="0 0 16 16" aria-hidden="true"><rect x="4" y="1" width="8" height="14" rx="1.5" fill="none" stroke="var(--icon-blue)" stroke-width="1.8"/><circle cx="8" cy="12.3" r="0.9" fill="var(--icon-blue)"/></svg>
        555 010 20 30
      </li>
      <li>
        <svg viewBox="0 0 16 16" aria-hidden="true"><rect x="1" y="3" width="14" height="10" fill="var(--icon-blue)"/><path d="M1 3 L8 9 L15 3" fill="none" stroke="#fff" stroke-width="1.3"/></svg>
        mrenwick@norvale.com
      </li>
    </ul>

    <ul class="contact-list contact-online">
      <li>
        <svg viewBox="0 0 16 16" aria-hidden="true"><rect x="1" y="1" width="14" height="14" rx="2" fill="var(--icon-blue)"/></svg>
        @Norvale
      </li>
      <li>
        <svg viewBox="0 0 16 16" aria-hidden="true"><circle cx="8" cy="8" r="6.5" fill="none" stroke="var(--icon-blue)" stroke-width="1.6"/><ellipse cx="8" cy="8" rx="2.8" ry="6.5" fill="none" stroke="var(--icon-blue)" stroke-width="1.2"/><path d="M1.5 8 H14.5" stroke="var(--icon-blue)" stroke-width="1.2"/></svg>
        www.Norvale.com
      </li>
    </ul>

    <div class="band"></div>
  </section>
</body>
</html>
```